Advertising flyer for proofreading business.

Hello everyone,

I need an advertising flyer for a new proofreading company in Australia.

I would like your design in be in two sizes:
- A4 (to be posted on noticeboards),
- A6 (to be printed in larger quantity to give away)
(please see the size specification file attached).

The text file is attached (Ad Text) and it contains lots of information. Please feel free to include your choice of text from the text file, but please include Poster title, and highlight 'ESL' and students discounts.

I understand that it is impossible to include the same amount of information on A6 and A4, so please feel free to chose what fits on each of them, but please keep the design similar.

I have attached our company logo, but feel free to adjust it to the poster design (feel free to change the color as well). The original logo file contains circle around it, please feel free to remove it and include only the typeset as it can be seen here: http://www.lexmarka.com.au/.

Flyers will be printed, so please see the specification file for details.

I will do my best to respond to feedback as soon as possible.

I appreciate your participation, time and help,
Best wishes,
Bartosz

Target Market(s)

Students, authors

Industry/Entity Type

Business

Colors

Designer to choose colors to be used in the design.

Requirements
Must have
• It would be good if poster is easy to spot on busy noticeboards and attract attention.
• Please keep the poster in the positive/optimistic mood, and so that it focuses on students, maybe photos of graduates(?).
• Poster title,
• Please include the list of proof-read documents as they are described in the attached text file (Ad Text).
• Please highlight students discounts and ESL.
Nice to have
• I would like to leave the creative freedom to all designers so at this point I have not adjusted the Look and Feel sliders. Please feel free to offer your own take on this.
• It would be nice if most of the text could be fit to the poster.

```html
<!DOCTYPE html>
<html lang="en">
<head>
<meta charset="utf-8">
<title>Lexmarka – Professional Proofreading Services</title>
<link rel="stylesheet" href="https://fonts.googleapis.com/css2?family=Montserrat:wght@400;500;600;700;800&display=swap">
<style>
  :root {
    --stage: #1e1e1e;
    --paper: #ffffff;
    --teal: #3aa88e;
    --teal-light: #45c2a2;
    --navy: #1f1f66;
    --navy-light: #2a2a7a;
    --grey: #8e8e96;
    --grey-light: #b4b4ba;
    --ink: #1a1a1a;
    --body: #3a3a3a;
  }
  * { box-sizing: border-box; margin: 0; padding: 0; }
  html, body { width: 1200px; height: 1000px; overflow: hidden; }
  body {
    background: var(--stage);
    font-family: "Montserrat", Arial, sans-serif;
    position: relative;
  }
  .flyer {
    position: absolute;
    left: 270px; top: 35px;
    width: 660px; height: 928px;
    background: var(--paper);
    overflow: hidden;
  }
  .flyer-shapes { position: absolute; inset: 0; }
  .brand-title {
    position: absolute; left: 40px; top: 26px;
    font-size: 54px; font-weight: 800; color: var(--teal);
    letter-spacing: 1px; line-height: 1;
  }
  .brand-subtitle {
    position: absolute; left: 40px; top: 88px; width: 330px;
    text-align: center; font-size: 17px; font-weight: 800;
    color: var(--ink); line-height: 21px; letter-spacing: 0.5px;
  }
  .intro {
    position: absolute; left: 27px; top: 526px; width: 220px;
    font-size: 12.6px; line-height: 18px; color: var(--body);
    font-weight: 500;
  }
  .intro p { margin-bottom: 17px; text-align: justify; }
  .intro strong { color: var(--ink); font-weight: 700; }
  .doc-types {
    position: absolute; left: 272px; top: 540px; width: 150px;
    color: #fff;
  }
  .panel-heading {
    font-size: 12.5px; font-weight: 700; color: var(--teal-light);
    line-height: 14px; letter-spacing: 0.3px;
  }
  .doc-list { list-style: none; margin-top: 12px; }
  .doc-list li {
    position: relative; padding-left: 14px;
    font-size: 10px; line-height: 11.5px; margin-bottom: 16px; font-weight: 500;
  }
  .doc-list svg { position: absolute; left: 0; top: -1px; width: 11px; height: 11px; }
  .price-guide {
    position: absolute; left: 450px; top: 504px; width: 196px;
    color: #fff;
  }
  .price-guide .panel-heading { font-size: 13px; margin-bottom: 4px; }
  .price-guide p {
    font-size: 9.6px; line-height: 11.6px; margin-left: 11px;
    margin-bottom: 11px; font-weight: 500;
  }
  .price-guide p:last-child { margin-bottom: 0; }
  .accent { color: var(--teal-light); font-weight: 600; }
  .contact {
    position: absolute; right: 18px; top: 795px; text-align: right;
    color: var(--ink);
  }
  .contact-lead { font-size: 15.5px; font-weight: 400; line-height: 18px; }
  .contact-lead strong { font-weight: 600; }
  .contact-phone {
    display: flex; align-items: center; justify-content: flex-end; gap: 4px;
    font-size: 34px; font-weight: 500; margin-top: 6px; line-height: 40px;
  }
  .contact-phone svg { width: 24px; height: 24px; }
  .contact-email { font-size: 20px; font-weight: 500; line-height: 26px; }
  .brand-badge {
    position: absolute; left: 52px; top: 752px;
    width: 152px; height: 152px; border-radius: 50%;
    background: var(--teal);
    display: flex; align-items: center; justify-content: center;
  }
  .brand-badge span { font-size: 25px; font-weight: 600; color: #fff; }
</style>
</head>
<body>
<div class="flyer">
  <svg class="flyer-shapes" viewBox="0 0 660 928" width="660" height="928">
    <defs>
      <linearGradient id="photoTone" x1="0" y1="0" x2="1" y2="0.4">
        <stop offset="0" stop-color="#d8dde3"/>
        <stop offset="0.35" stop-color="#e9c9b2"/>
        <stop offset="0.6" stop-color="#3a3d48"/>
        <stop offset="1" stop-color="#23262e"/>
      </linearGradient>
      <linearGradient id="greyBand" x1="0" y1="0" x2="1" y2="0">
        <stop offset="0" stop-color="#b4b4ba"/>
        <stop offset="1" stop-color="#8e8e96"/>
      </linearGradient>
    </defs>
    <path class="corner-swoosh" d="M465 0 H660 V370 Q650 150 560 60 Q520 20 465 0 Z" fill="var(--teal)"/>
    <path class="hero-photo" role="img"
      aria-label="Photo: a hand writing with a pen on paper beside two smiling graduates in black gowns and mortarboards"
      d="M0 135 H300 Q360 128 420 110 Q520 70 590 40 Q640 60 660 110 V330 Q560 430 420 465 Q250 495 0 470 Z"
      fill="url(#photoTone)"/>
    <path class="teal-band" d="M0 468 Q250 494 420 463 Q540 435 610 390 Q520 460 420 480 Q250 510 0 490 Z" fill="var(--teal)"/>
    <path class="grey-swoosh" d="M290 515 Q520 490 660 330 V420 Q540 510 300 522 Z" fill="url(#greyBand)"/>
    <path class="navy-panel" d="M262 524 Q480 508 660 430 V928 H262 Z" fill="var(--navy)"/>
    <path class="navy-column" d="M440 505 Q560 480 660 430 V740 H440 Z" fill="var(--navy-light)"/>
    <path class="contact-edge" d="M262 928 Q380 760 660 738 V750 Q390 770 280 928 Z" fill="#fff"/>
    <path class="contact-panel" d="M280 928 Q390 770 660 750 V928 Z" fill="url(#greyBand)"/>
  </svg>

  <h1 class="brand-title">LEXMARKA</h1>
  <h2 class="brand-subtitle">PROFESSIONAL PROOFREADING SERVICES</h2>

  <div class="intro">
    <p>Help with English as a second language <strong>(ESL - native English speaker with English Honours</strong> degree will correct all English language errors, spelling and grammar mistakes.</p>
    <p>Includes referencing and editing for style, coherence and clarity</p>
    <p>Fast, negotiable time-frames.</p>
  </div>

  <div class="doc-types">
    <h3 class="panel-heading">TYPES OF PROOF-READ DOCUMENTS:</h3>
    <ul class="doc-list">
      <li><svg viewBox="0 0 12 12"><path d="M1 6 L4.5 10 L11 1" fill="none" stroke="var(--teal-light)" stroke-width="2"/></svg>essays / assignments / theses / resumes</li>
      <li><svg viewBox="0 0 12 12"><path d="M1 6 L4.5 10 L11 1" fill="none" stroke="var(--teal-light)" stroke-width="2"/></svg>business correspondence / training manuals / newsletters</li>
      <li><svg viewBox="0 0 12 12"><path d="M1 6 L4.5 10 L11 1" fill="none" stroke="var(--teal-light)" stroke-width="2"/></svg>advertising copy / brochures / catalogues / media releases</li>
      <li><svg viewBox="0 0 12 12"><path d="M1 6 L4.5 10 L11 1" fill="none" stroke="var(--teal-light)" stroke-width="2"/></svg>websites / presentations / speeches</li>
      <li><svg viewBox="0 0 12 12"><path d="M1 6 L4.5 10 L11 1" fill="none" stroke="var(--teal-light)" stroke-width="2"/></svg>novels / short stories</li>
    </ul>
  </div>

  <div class="price-guide">
    <h3 class="panel-heading">PRICE GUIDE:</h3>
    <p>Prices starting at <span class="accent">$20 per page.</span> Additional charges may apply for longer and/or more complex documents (e.g. documents requiring specialist help with English as a second language).</p>
    <p>Discounts for not-for-profit organisations and students. <span class="accent">Special student discount rate: $25 per hour - roughly 1000 words (4 pages) of well-written text.</span></p>
    <p>Package deals on documents <span class="accent">over 50,000 words.</span></p>
    <p>Fast turnaround times (same day service can be provided by special arrangement).</p>
  </div>

  <div class="contact">
    <p class="contact-lead">Contact Us For An<br><strong>Obligation-Free Quote:</strong></p>
    <p class="contact-phone">
      <svg viewBox="0 0 24 24"><circle cx="12" cy="12" r="10.5" fill="none" stroke="var(--navy)" stroke-width="2"/><path d="M8.5 6.5 L10.5 9 L9.3 10.5 Q10.5 13 13.5 14.7 L15 13.5 L17.5 15.5 L16 17.5 Q11 17 7.5 11.5 Q6.8 8 8.5 6.5 Z" fill="var(--navy)"/></svg>
      0400 555 018
    </p>
    <p class="contact-email">proofing@lexmarka.com.au</p>
  </div>

  <div class="brand-badge"><span>Lexmarka</span></div>
</div>
</body>
</html>
```